Elegant and modern Wedding Photography brochure

My existing brochure (attached) needs a major facelift. This is one of the main selling tools - it gets emailed to my clients when they make an equiry on what packages i offer and it is printed out and walked through at our first meeting. This brochure is as critical as my website - it needs to sing!

I'm looking for an eye-catching design that says:
Elegant
Modern
Clean
Crisp
Not cutesy or lovey-dovey thanks - we are more sophisticated and professional than that.

Update images to some of the latest weddings I've shot also. Let me know files and resolution you need. I've enabled right-click to download images on my site for a limited time. Please note that I retain copyright and will pursue any breeches.

Http://www.carlathornbey.com/Melbourne-wedding-photography
Updates

Thanks for all of your designs! Will take a few days to decide.

Target Market(s)

Australian Women aged 24-44

Industry/Entity Type

Wedding

Font styles to use
Other font styles liked:
• Century Gothic

Requirements
Must have
• Easy to print - does not have to be 6 A4 pages like the existing brochure
Nice to have
• Some full page images - The photos are supposed to be the hero here :-)
Should not have
• Not cutesy or lovey-dovey thanks - we are more sophisticated and professional than that.

No black backgrounds, I prefer a white thanks

No images in organic shaped boxes (like the rectangles in the logo - no thanks).
Keep the lines straight and sharp

```html
<!DOCTYPE html>
<html lang="en">
<head>
<meta charset="utf-8">
<title>Carla Thornbey – Wedding Brochure</title>
<link href="https://fonts.googleapis.com/css2?family=Questrial&family=Cormorant+Garamond:wght@600&display=swap" rel="stylesheet">
<style>
:root{
  --bg:#ece9e5;
  --paper:#ffffff;
  --plum:#8e2a8a;
  --ink:#5a5a5a;
  --soft:#8a8a8a;
  --peach:#f4dccc;
  --blush:#f8e6dc;
  --teal:#72c6ae;
  --mustard:#c8b620;
  --orchid:#a54aa0;
}
*{margin:0;padding:0;box-sizing:border-box}
html,body{width:1200px;height:760px;overflow:hidden;background:var(--bg)}
body{position:relative;font-family:"Questrial",sans-serif;color:var(--ink)}
.page,.abs{position:absolute}
.page{background:var(--paper);overflow:hidden;box-shadow:0 2px 6px rgba(0,0,0,.18)}
.photo{position:absolute}
.spine{position:absolute;top:0;bottom:0;width:4px;background:var(--plum);z-index:2}
.ph-veil{background:radial-gradient(ellipse at 62% 70%,#f4f4f4 0,#d6d6d6 28%,#8c8c8c 62%,#3c3c3c 100%)}
.ph-hands{background:linear-gradient(100deg,#1e1e1e 0,#3a3a3a 30%,#9a9a9a 48%,#e8e8e8 66%,#bdbdbd 100%)}
.ph-bw{background:linear-gradient(90deg,#2a2a2a 0,#6f6f6f 22%,#dcdcdc 50%,#9e9e9e 70%,#3c3c3c 100%)}
.ph-roses{background:radial-gradient(ellipse at 48% 62%,#f1b9b6 0,#f5d4cc 28%,#f9ebe4 58%,#fbf5f1 100%)}
.ph-bride{background:radial-gradient(ellipse at 45% 70%,#f7f5f0 0,#d9d4c9 35%,#8f8a7d 70%,#5a5650 100%)}
.ph-willow{background:linear-gradient(180deg,#3d4220 0,#6b6a2c 25%,#8a8640 42%,#c9c4b2 58%,#f0ede6 70%,#4e3b28 88%,#2f2418 100%)}
.ph-willow-sm{background:linear-gradient(90deg,#3d4220 0,#7a7534 30%,#e9e5dc 52%,#2a2a2a 68%,#6b6a2c 100%)}
.ph-party{background:linear-gradient(180deg,#4a4a28 0,#6d6a3c 30%,#2a2540 52%,#352e4a 62%,#f4f1ec 80%,#e7e2da 100%)}
.ph-stone{background:linear-gradient(90deg,#4a3a2c 0,#7d6a54 22%,#1f1f22 42%,#f2eee8 60%,#8a7763 78%,#54463a 100%)}
.ph-groomsmen{background:linear-gradient(180deg,#cfcfcf 0,#a9a9a9 30%,#2a2a2a 55%,#1a1a1a 80%,#6e6e6e 100%)}
.ph-pkg{background:radial-gradient(ellipse at 85% 8%,#f1c8c6 0,#f5e0dc 30%,#efe3dc 55%,#cdb8aa 85%,#9c8a7e 100%)}
.logo{display:flex;align-items:center;gap:4px;color:var(--plum);font-size:8px;letter-spacing:.2px}
.logo i{display:block;width:8px;height:8px;border:1px solid currentColor}
h2.title{font-weight:400;color:var(--plum);line-height:1}
.kicker{color:var(--plum);font-size:6px;text-transform:uppercase;letter-spacing:.2px;margin-top:6px}
.body{font-size:5.6px;line-height:1.48;color:var(--ink)}
.folio{position:absolute;bottom:8px;font-size:4.5px;color:var(--soft)}
.cover{background:var(--peach)}
.cover-line{font-family:"Cormorant Garamond",serif;font-weight:600;color:#1e1e1e;font-size:15px;line-height:1.2;letter-spacing:.6px;text-align:center}
.pkg{position:absolute;left:22px;width:182px;color:#fff;padding:5px 8px}
.pkg h3{font-weight:400;font-size:10px;line-height:1}
.pkg .price{font-size:5px;font-style:italic;margin:2px 0 4px;opacity:.9}
.pkg ul{list-style:none;display:grid;grid-template-columns:1.2fr 1fr;column-gap:10px;font-size:3.6px;line-height:1.45}
.pkg li::before{content:"• "}
.pkg li:empty::before{content:""}
.fees dt{color:var(--plum);font-size:4.6px;text-transform:uppercase;margin-top:2px}
.fees dd{font-size:4.6px;line-height:1.4;color:var(--ink)}
.quote{font-size:5.6px;line-height:1.5}
.quote cite{display:block;font-style:normal;color:var(--plum);text-transform:uppercase;font-size:5px;margin-top:1px}
</style>
</head>
<body>

<section class="page cover" style="left:33px;top:61px;width:216px;height:312px">
  <div class="photo ph-veil" role="img" aria-label="Black and white photo of a bride in her veil" style="left:5px;top:4px;width:206px;height:107px"></div>
  <div class="abs cover-line" style="left:48px;top:55px;width:120px">LOVE IS ALL<br>YOU NEED</div>
  <div class="photo ph-hands" role="img" aria-label="Black and white photo of the couple holding hands" style="left:5px;top:115px;width:206px;height:94px"></div>
  <div class="photo ph-roses" role="img" aria-label="Bouquet of pale pink roses" style="left:5px;top:213px;width:206px;height:95px"></div>
  <div class="abs logo" style="left:12px;top:224px;color:#8a6e8a"><i></i>Carla Thornbey</div>
</section>

<section class="page" style="left:266px;top:62px;width:220px;height:311px">
  <h2 class="title abs" style="left:19px;top:44px;font-size:12px">Carla’s<br>approach…</h2>
  <p class="abs" style="left:19px;top:76px;font-size:7px;color:var(--plum);font-style:italic">Enjoy your special day!</p>
  <div class="abs" style="left:19px;top:86px;width:92px">
    <p class="kicker">Style &amp; approach</p>
    <p class="body">Carla can observe and capture your wedding day in the background, quickly and quietly taking photojournalistic pictures rather than directing it if you prefer. Or she can confidently play the role of Art Director and instruct beautiful poses. Either way, what is most important is that her clients are relaxed and having a really great time on their wedding day!</p>
    <p class="kicker">Formal photography</p>
    <p class="body">Many of Carla’s clients book her because of the easy-going approach she has. They can get on with having a great time on their day without worrying about formal photography. However, there are occasions when clients do want formal family pictures, and</p>
  </div>
  <div class="photo ph-bride" role="img" aria-label="Bride holding a rose bouquet" style="left:112px;top:18px;width:88px;height:147px"></div>
  <div class="abs" style="left:114px;top:170px;width:90px">
    <p class="body">Carla is more than happy to accommodate their requests. In order to keep the disruption on the day to a minimum, we recommend that Carla photographs no more than 6 groups, and a select number of the special couple.</p>
    <p class="kicker">Image presentation</p>
    <p class="body">The most professional way of presenting clients with their photographs is in an elegantly designed photo book.</p>
  </div>
  <span class="folio" style="left:108px">2</span>
</section>
<section class="page" style="left:486px;top:62px;width:218px;height:311px">
  <div class="spine" style="left:0"></div>
  <div class="abs" style="left:18px;top:20px;width:88px">
    <p class="body">Carla’s clients only pay one fixed price for the photography, regardless of how many images taken. There are no hard sell procedures to go through, and the completed book is prepared within 2-6 weeks after the wedding day.</p>
  </div>
  <div class="abs" style="left:112px;top:20px;width:92px">
    <p class="kicker" style="margin-top:0">Time of year</p>
    <p class="body">Signature pictures can be taken on overcast days or winter months. Don’t worry if the sky is not perfectly blue. In the end, regardless of the weather – it’s the timeless mood of the day that Carla strives to capture.</p>
  </div>
  <div class="photo ph-willow" role="img" aria-label="Bride and groom under willow trees by a fallen log" style="left:4px;top:108px;width:214px;height:203px"></div>
</section>

<section class="page" style="left:718px;top:61px;width:218px;height:312px">
  <div class="photo ph-party" role="img" aria-label="Laughing bride with bridesmaids in navy dresses" style="left:0;top:0;width:218px;height:191px"></div>
  <h2 class="abs" style="left:19px;top:35px;font-weight:400;font-size:12px;line-height:.95;color:#fff">What client’s<br>are saying…</h2>
  <div class="abs quote" style="left:20px;top:210px;width:88px">“Words can’t express my thanks Carla, I am absolutely in awe of my photos! You’ve captured my wedding day perfectly; couldn’t ask for anything more.”<cite>-Tess, Seddon</cite></div>
  <div class="abs quote" style="left:114px;top:208px;width:94px">“Thanks so much for photographing our special day, you did an amazing job and made everyone feel so comfortable. The amount of comments we have had on the photos so far has been wonderful and we couldn’t be happier!”<cite>-Marnie, Kingsville</cite></div>
  <span class="folio" style="left:107px">4</span>
</section>
<section class="page ph-pkg" role="img" aria-label="Soft pink roses in a glass vase" style="left:936px;top:61px;width:223px;height:312px">
  <div class="spine" style="left:0"></div>
  <h2 class="title abs" style="left:22px;top:18px;font-size:13px">Wedding Packages</h2>
  <p class="abs" style="left:22px;top:35px;font-size:7px;font-style:italic;color:var(--soft)">Pricelist 2013</p>
  <div class="pkg" style="top:53px;height:84px;background:var(--orchid)">
    <h3>Signature</h3><p class="price">Price: $3650 ($5540 value)</p>
    <ul><li>Up to 8 hrs of coverage</li><li>Client for life (no sitting fees)</li><li>Signature Grand (A3) Album with lay-flat pages and leather cover, presentation box, up to 52 pages</li><li>Second photographer</li><li>Custom thank-you cards with envelopes (50)</li><li>Pre-wedding shoot</li><li></li><li>Web gallery (online for 6 weeks) &amp; social media</li><li></li><li>High resolution digital negatives*</li></ul>
  </div>
  <div class="pkg" style="top:138px;height:65px;background:var(--teal)">
    <h3>Platinum</h3><p class="price">Price: $2300 ($3440 value)</p>
    <ul><li>Up to 6 hrs of coverage</li><li>Pre-wedding shoot</li><li>Regular (A4) Album with lay-flat pages, printed cover, presentation box, up to 40 pages</li><li>Web gallery (online for 6 weeks) &amp; social media</li><li>Slideshow</li><li>High resolution digital negatives*</li></ul>
  </div>
  <div class="pkg" style="top:204px;height:58px;background:var(--mustard)">
    <h3>Gold</h3><p class="price">Price: $1650 ($2580 value)</p>
    <ul><li>Up to 4 hrs of coverage</li><li>Web gallery (online for 6 weeks) &amp; social media</li><li>Regular (A4) Album with lay-flat pages, printed cover, presentation box, up to 32 pages</li><li>High resolution digital negatives*</li></ul>
  </div>
  <p class="abs" style="left:22px;top:283px;font-size:3.6px;color:#fff">* Approx. 1200×800 pixels at 240 ppi, suitable for prints. No watermarks.</p>
  <span class="folio" style="left:110px;color:#fff">5</span>
</section>

<section class="page" style="left:266px;top:399px;width:220px;height:311px">
  <div class="photo ph-willow-sm" role="img" aria-label="Couple walking beneath willow trees" style="left:0;top:0;width:131px;height:75px"></div>
  <div class="photo ph-bride" role="img" aria-label="Portrait of the bride smiling" style="left:132px;top:0;width:88px;height:75px"></div>
  <h2 class="title abs" style="left:19px;top:96px;font-size:12px">À la carte<br>Fees to consider</h2>
  <dl class="abs fees" style="left:21px;top:130px;width:190px">
    <dt>Engagement session/pre-wedding shoot</dt><dd>$290 for up to 2 hours of photography on location</dd>
    <dt>Digital negatives <span style="color:var(--ink)">$490</span></dt>
    <dt>Extended coverage <span style="color:var(--ink);text-transform:none">$160 per hour</span></dt>
    <dt>Web gallery &amp; social media posting <span style="color:var(--ink)">$160</span></dt>
    <dt>Slideshow <span style="color:var(--ink)">$250</span></dt>
    <dt>Second photographer <span style="color:var(--ink)">$590</span></dt>
    <dt>Client for life</dt><dd>No sitting fees for portrait sessions – Anniversaries, family portraits, etc: $390</dd>
    <dt>Photo enlargements</dt><dd>- Quality custom archival prints in a variety of sizes 5x7 up to 8x10 $25, 12.5x18.5 $50<br>- Stretched canvas prints for your wall. Various sizes available from 16"x20" starting at $395 through to 60"x96" $1500<br>Plus many other options!</dd>
    <dt>Professionally edited album (regular) <span style="color:var(--ink)">$790</span></dt>
    <dt>Album upgrade from regular to signature grand</dt><dd>- From Gold Package to Signature Grand: $1150<br>- From Platinum Package to Signature Grand: $650</dd>
    <dt>Custom thank-you cards</dt><dd>$150 for 50 cards (174mm x 123mm) including envelopes</dd>
  </dl>
  <span class="folio" style="left:108px">6</span>
</section>
<section class="page" style="left:486px;top:399px;width:218px;height:311px">
  <div class="spine" style="left:0"></div>
  <div class="abs logo" style="left:80px;top:20px"><i></i>Carla Thornbey</div>
  <h2 class="title abs" style="left:17px;top:53px;font-size:11px;letter-spacing:.3px">HOW DO YOU WANT<br>TO REMEMBER…</h2>
  <div class="photo ph-bw" role="img" aria-label="Black and white portrait of the bride and groom embracing" style="left:4px;top:75px;width:214px;height:142px"></div>
  <p class="abs" style="left:64px;top:196px;font-size:11px;color:var(--plum);letter-spacing:.3px">YOUR SPECIAL DAY?</p>
  <div class="abs body" style="left:17px;top:232px;width:190px;font-size:4.8px">
    <p>Elegant, stunning, fuss-free photography that doesn’t cost the earth will capture those memories for a lifetime!<br>Wedding photography packages start from $1650 and are fully inclusive of fun-filled creative &amp; journalistic coverage, digital negatives and professionally edited album.</p>
    <p style="margin-top:5px">Contact Carla today to arrange an informal catch-up, discuss your requirements and find out more about the <span style="color:var(--plum)">early booking bonus!</span></p>
  </div>
  <span class="folio" style="left:106px">7</span>
</section>

<section class="page" style="left:720px;top:399px;width:218px;height:311px;background:var(--blush);border-bottom:4px solid var(--plum)">
  <div class="abs" style="left:0;top:0;width:218px;height:234px;background:var(--paper)"></div>
  <div class="photo ph-party" role="img" aria-label="Bride with bridesmaids holding bouquets" style="left:4px;top:5px;width:104px;height:102px"></div>
  <div class="photo ph-groomsmen" role="img" aria-label="Black and white photo of the groom with groomsmen" style="left:112px;top:5px;width:102px;height:102px"></div>
  <div class="photo ph-stone" role="img" aria-label="Couple in front of an old stone building" style="left:4px;top:114px;width:210px;height:115px"></div>
  <div class="abs logo" style="left:72px;top:254px"><i></i>Carla Thornbey</div>
  <p class="abs" style="left:0;width:218px;top:282px;text-align:center;font-size:4.4px;color:var(--ink)">12 Linden Street, Seddon, VIC, 3011</p>
  <p class="abs" style="left:0;width:218px;top:293px;text-align:center;font-size:4.4px;color:var(--plum);word-spacing:1px">www.carlathornbey.com &nbsp; · &nbsp; carla@carlathornbey.com &nbsp; · &nbsp; Mobile: 0400 000 123</p>
</section>

</body>
</html>
```